Business Card for Orthopaedic Clinic.
Should have nice design, double sided that includes logo
Should include my name, my contact, my email, webpage. A QR code to scan business card.

please use dummy information for privacy reasons. I will provide my name, email, practice address once a winner is selected.

Target Market(s)

Future patients

Contact Information for Business Card

Name: Dr Ruk
Contact No: +65 90417263
Practice Address: Singapore
Email: doctor@brevlo.com
Website: www.brevlo.com

Colors
00a990

Requirements
Must have
• Logo and a nice colour scheme.
A QR Code for Contact Card.
Name
Contact
Practice Address
Email
Website.
Nice to have
• Nice colour scheme
Should not have
• Nothing too cluttered.

```html
<!DOCTYPE html>
<html lang="en">
<head>
<meta charset="utf-8">
<title>Brevlo Orthopaedics – Business Card</title>
<link rel="stylesheet" href="https://fonts.googleapis.com/css2?family=Oswald:wght@500&family=Roboto:wght@400&display=swap">
<style>
  :root{
    --stage:#2a2b2d;
    --white:#ffffff;
    --teal:#5ab7b2;
    --teal-deep:#4a9e9a;
    --slate:#5b6670;
    --card-back:#5d6770;
    --emboss:#4b545c;
  }
  *{margin:0;padding:0;box-sizing:border-box}
  html,body{width:1200px;height:1200px;overflow:hidden;background:var(--stage)}
  .canvas{position:relative;width:1200px;height:1200px}
  .card{
    position:absolute;left:262px;width:686px;height:392px;
    border-radius:0 26px 0 26px;overflow:hidden;
  }
  .card--front{top:165px;background:var(--white)}
  .card--back{top:653px;background:var(--card-back)}
  .card__accent{position:absolute;inset:0;width:100%;height:100%}

  .brand{position:absolute;display:flex;align-items:center;gap:14px}
  .brand__mark{flex:none}
  .brand__name{font-family:"Roboto",sans-serif;font-weight:400;line-height:1;white-space:nowrap}

  .card--front .brand{left:51px;top:101px}
  .card--front .brand__mark{width:34px;height:34px;background:var(--teal)}
  .card--front .brand__name{color:var(--slate);font-size:30px}

  .card--back .brand{left:50%;top:50%;transform:translate(-50%,-50%)}
  .card--back .brand__mark{width:40px;height:40px;background:var(--emboss)}
  .card--back .brand__name{color:var(--emboss);font-size:36px}

  .holder{position:absolute;right:47px;top:225px;text-align:right;color:var(--white)}
  .holder__name{font-family:"Oswald",sans-serif;font-weight:500;font-size:31px;line-height:1;letter-spacing:.5px;text-transform:uppercase;margin-bottom:10px}
  .contact{list-style:none;font-family:"Roboto",sans-serif;font-size:17px;line-height:1}
  .contact__item{display:flex;justify-content:flex-end;align-items:center;gap:9px;height:22px}
  .contact__item--place{margin-bottom:11px}
  .contact__icon{width:14px;height:14px;flex:none}
</style>
</head>
<body>
<div class="canvas">

  <section class="card card--front">
    <svg class="card__accent" viewBox="0 0 686 392" preserveAspectRatio="none" role="img" aria-label="Teal accent area carrying the contact details">
      <defs>
        <linearGradient id="accentFill" x1="0" y1="1" x2="1" y2="0">
          <stop offset="0" stop-color="var(--teal-deep)"/>
          <stop offset="1" stop-color="var(--teal)"/>
        </linearGradient>
      </defs>
      <path fill="url(#accentFill)" d="M0,392 L0,330 C220,330 420,130 686,120 L686,392 Z"/>
    </svg>

    <div class="brand">
      <span class="brand__mark"></span>
      <span class="brand__name">Brevlo Orthopaedics</span>
    </div>

    <div class="holder">
      <h1 class="holder__name">Dr Ruk</h1>
      <ul class="contact">
        <li class="contact__item contact__item--place">Singapore
          <svg class="contact__icon" viewBox="0 0 14 14"><path fill="#fff" d="M7 0a5 5 0 0 0-5 5c0 3.6 5 9 5 9s5-5.4 5-9a5 5 0 0 0-5-5zm0 7.2A2.2 2.2 0 1 1 7 2.8a2.2 2.2 0 0 1 0 4.4z"/></svg>
        </li>
        <li class="contact__item">+65 90417263
          <svg class="contact__icon" viewBox="0 0 14 14"><path fill="#fff" d="M3 0.5l2.3 2.8-1.3 1.6c.8 1.9 2.2 3.4 4.1 4.3l1.6-1.3 2.8 2.3-1.2 2.3C6.3 12.3 1.6 7.7 0.7 1.7z"/></svg>
        </li>
        <li class="contact__item">doctor@brevlo.com
          <svg class="contact__icon" viewBox="0 0 14 14"><path fill="#fff" d="M1 3h12v1.2L7 8 1 4.2z M1 5.6l6 3.8 6-3.8V11H1z"/></svg>
        </li>
        <li class="contact__item">www.brevlo.com
          <svg class="contact__icon" viewBox="0 0 14 14"><circle cx="7" cy="7" r="6.5" fill="#fff"/><path fill="var(--teal)" d="M1 7h12M7 1c-2.2 2.2-2.2 9.8 0 12M7 1c2.2 2.2 2.2 9.8 0 12" stroke="var(--teal)" stroke-width="1" fill="none"/></svg>
        </li>
      </ul>
    </div>
  </section>

  <section class="card card--back">
    <div class="brand">
      <span class="brand__mark"></span>
      <span class="brand__name">Brevlo Orthopaedics</span>
    </div>
  </section>

</div>
</body>
</html>
```